Korvanta IT Service Management Business Card Design

We need a business card design for an IT Service Management consulting company that is a certified partner of an ITSM software vendor.
The company name: Korvanta
Vendor whom Korvanta is a certified partner of: MoorPlex
Visit http://www.korvantaops.example
Visit http://www.moorplex.example
Industry/Entity Type
Software
Contact Information for Business Card
Front Content: (blue and white)
- Korvanta Logo (attached)
- Korvanta
- IT Service Management
- Dale Pruett
- (555) 301-4827 - office
- (555) 768-2093 - mobile
- dale@korvantaops.example
- www.korvantaops.example
- 2870 Bramwick Pkwy., #5317
Lilburn, GA 30099
Back Content: (blue and green)
- Moorplex Prime Certified partner logo (attached)
- IT Service Management
- IT Asset Management
- IT Financial Management
(place the 3 items above in blocks of different colors - see attached sample)
Look and feel
Each slider illustrates characteristics of the customer's brand and the style your logo design should communicate.

```html
<!DOCTYPE html>
<html lang="en">
<head>
<meta charset="utf-8">
<title>Korvanta Business Card</title>
<link rel="stylesheet" href="https://fonts.googleapis.com/css2?family=Exo+2:wght@400;500;600&display=swap">
<style>
  :root {
    --page-bg: #e9ebef;
    --card-white: #ffffff;
    --brand-blue: #2c4f93;
    --brand-navy: #263f7a;
    --swoosh-light: #b9c8e3;
    --partner-green: #4c9a3f;
    --block-teal: #2f8f8a;
    --text-on-blue: #ffffff;
  }
  * { margin: 0; padding: 0; box-sizing: border-box; }
  html, body {
    width: 1200px; height: 899px; overflow: hidden;
    background: var(--page-bg);
    font-family: "Exo 2", sans-serif;
  }
  .canvas { position: relative; width: 1200px; height: 899px; }
  .card {
    position: absolute; left: 240px;
    width: 720px; height: 412px;
    border-radius: 52px; overflow: hidden;
    background: var(--card-white);
    box-shadow: 0 10px 28px rgba(30, 40, 70, 0.18);
  }
  .card-front { top: 28px; }
  .card-back { top: 459px; }
  .card-shapes { position: absolute; inset: 0; width: 100%; height: 100%; }

  .brand {
    position: absolute; left: 52px; top: 128px;
    display: flex; flex-direction: column; align-items: flex-start;
  }
  .brand-name {
    display: flex; align-items: center; gap: 11px;
    font-size: 58px; font-weight: 600; color: var(--brand-navy);
    line-height: 1;
  }
  .brand-dot {
    width: 18px; height: 18px; border-radius: 50%;
    background: var(--brand-navy);
  }
  .brand-tagline {
    margin-top: 8px; margin-left: 29px;
    font-size: 14px; font-weight: 500; color: var(--brand-navy);
  }

  .details {
    position: absolute; left: 446px; top: 52px;
    color: var(--text-on-blue);
  }
  .person-name { font-size: 21px; font-weight: 500; letter-spacing: 1px; text-transform: uppercase; }
  .address { margin-top: 40px; font-size: 16px; line-height: 1.35; }
  .contact-list { list-style: none; margin-top: 40px; }
  .contact-list li {
    display: flex; align-items: center; gap: 11px;
    font-size: 14px; height: 30px;
  }
  .contact-list .label { opacity: 0.8; }
  .contact-list svg { width: 15px; height: 15px; flex: none; fill: none; stroke: var(--text-on-blue); stroke-width: 2; }

  .back-brand {
    position: absolute; left: 48px; top: 56px;
    display: flex; align-items: center; gap: 9px;
    font-size: 30px; font-weight: 600; color: var(--brand-navy);
  }
  .back-brand .brand-dot { width: 11px; height: 11px; }
  .partner-badge {
    position: absolute; left: 78px; top: 160px;
    width: 150px; height: 150px; border-radius: 50%;
    background: var(--partner-green);
  }
  .service-blocks {
    position: absolute; right: 44px; top: 56px;
    width: 340px; list-style: none;
    display: flex; flex-direction: column; gap: 14px;
  }
  .service-blocks li {
    height: 90px; border-radius: 10px;
    display: flex; align-items: center; padding-left: 24px;
    font-size: 20px; font-weight: 500; color: var(--text-on-blue);
  }
  .block-service { background: var(--brand-blue); }
  .block-asset { background: var(--partner-green); }
  .block-finance { background: var(--block-teal); }
</style>
</head>
<body>
<div class="canvas">
  <section class="card card-front">
    <svg class="card-shapes" viewBox="0 0 900 514" preserveAspectRatio="none">
      <path d="M395 0 C500 110 505 330 20 514 L95 514 C520 350 510 110 430 0 Z" fill="var(--swoosh-light)"/>
      <path d="M450 0 C560 120 540 370 80 514 L900 514 L900 0 Z" fill="var(--brand-blue)"/>
    </svg>

    <div class="brand">
      <div class="brand-name"><span class="brand-dot"></span>Korvanta</div>
      <div class="brand-tagline">IT Service Management</div>
    </div>

    <div class="details">
      <div class="person-name">Dale Pruett</div>
      <div class="address">2870 Bramwick Pkwy., #5317<br>Lilburn, GA 30099</div>
      <ul class="contact-list">
        <li><svg viewBox="0 0 24 24"><path d="M5 3h4l2 5-3 2a12 12 0 0 0 6 6l2-3 5 2v4a2 2 0 0 1-2 2A18 18 0 0 1 3 5a2 2 0 0 1 2-2z"/></svg>(555) 301-4827 <span class="label">office</span></li>
        <li><svg viewBox="0 0 24 24"><rect x="7" y="2" width="10" height="20" rx="2"/><line x1="11" y1="18" x2="13" y2="18"/></svg>(555) 768-2093 <span class="label">mobile</span></li>
        <li><svg viewBox="0 0 24 24"><rect x="3" y="5" width="18" height="14" rx="1"/><path d="M3 6l9 7 9-7"/></svg>dale@korvantaops.example</li>
        <li><svg viewBox="0 0 24 24"><circle cx="12" cy="12" r="9"/><path d="M3 12h18M12 3c3 3 3 15 0 18M12 3c-3 3-3 15 0 18"/></svg>www.korvantaops.example</li>
      </ul>
    </div>
  </section>

  <section class="card card-back">
    <div class="back-brand"><span class="brand-dot"></span>Korvanta</div>
    <div class="partner-badge" role="img" aria-label="Moorplex Prime Certified partner badge"></div>
    <ul class="service-blocks">
      <li class="block-service">IT Service Management</li>
      <li class="block-asset">IT Asset Management</li>
      <li class="block-finance">IT Financial Management</li>
    </ul>
  </section>
</div>
</body>
</html>
```